Vault 9 Nook Storage Poster Ad

Vault 9 Nook Storage needs an 8.5" X 11" specialty storage products poster.

Graphics that illustrate seasonal tire storage, bicycle storage, and motorcycle storage.

Information on the poster will be as follows:

Tire storage: $99.00/season + tax
bicycle storage: $99.00/season + tax
motorcycle storage: $250.00/season + tax
Phone: 306-555-0148
Web: www.vault9nook.ca
Address: Vault 9 Nook Storage, 4718 Brindle Avenue, Saskatoon, SK, S4M 2J6

**Information does not need to be presented in this exact format. The designer can creatively list the services and the prices. The words phone, web, and address can be left out**

**The season that the ad is targeting is winter

Industry/Entity Type

Storage

```html
<!DOCTYPE html>
<html lang="en">
<head>
<meta charset="utf-8">
<title>Vault 9 Nook Storage – Seasonal Storage Poster</title>
<link rel="stylesheet" href="https://fonts.googleapis.com/css2?family=Josefin+Sans:ital,wght@0,400;0,600;0,700&display=swap">
<style>
  :root {
    --bg: #1c1c1c;
    --ink: #1c1c1c;
    --white: #f2f2f2;
    --grey-light: #b2b2b2;
    --grey-overlap: #e4e4e4;
    --grey-dark: #7f7f7f;
    --brand-red: #d22a25;
  }
  * { margin: 0; padding: 0; box-sizing: border-box; }
  html, body { width: 900px; height: 1200px; overflow: hidden; background: var(--bg); }
  .poster { display: block; width: 900px; height: 1200px; }
  .poster text { font-family: "Josefin Sans", "Futura", sans-serif; font-style: normal; }
  .bg { fill: var(--bg); }
  .block--light { fill: var(--grey-light); }
  .block--white { fill: var(--white); }
  .block--overlap { fill: var(--grey-overlap); }
  .block--dark { fill: var(--grey-dark); }
  .headline { font-size: 166px; font-weight: 600; fill: var(--ink); }
  .headline--light { fill: var(--white); }
  .word-storage { font-size: 162px; font-weight: 700; fill: var(--white); }
  .contact { font-size: 17px; font-weight: 700; fill: var(--white); letter-spacing: 0.6px; }
  .contact--phone { font-size: 21px; letter-spacing: 9px; }
  .contact--web { font-size: 19px; letter-spacing: 0.3px; }
  .divider { stroke: var(--white); stroke-width: 2; }
  .brand__mark { fill: var(--brand-red); }
  .brand__name { font-size: 25px; font-weight: 700; fill: var(--white); }
  .price__amount { font-size: 138px; font-weight: 600; fill: var(--ink); }
  .price__cents { font-size: 70px; font-weight: 600; fill: var(--ink); }
  .price__note { font-size: 27px; font-weight: 700; fill: var(--ink); }
</style>
</head>
<body>
<svg class="poster" viewBox="0 0 900 1200" width="900" height="1200" xmlns="http://www.w3.org/2000/svg" role="img" aria-label="Vault 9 Nook Storage seasonal storage prices">
  <rect class="bg" x="0" y="0" width="900" height="1200"/>

  <!-- colour blocks -->
  <rect class="block--light" x="252" y="437" width="428" height="190"/>
  <rect class="block--light" x="252" y="625" width="510" height="177"/>
  <rect class="block--white" x="760" y="260" width="105" height="732"/>
  <rect class="block--overlap" x="760" y="625" width="105" height="177"/>
  <rect class="block--dark" x="35" y="815" width="203" height="177"/>
  <rect class="block--dark" x="35" y="990" width="357" height="175"/>
  <rect class="block--white" x="507" y="990" width="358" height="175"/>

  <!-- vertical headline -->
  <text class="word-storage" transform="translate(198 785) rotate(-90)" x="0" y="0" textLength="745" lengthAdjust="spacingAndGlyphs">STORAGE</text>

  <!-- contact -->
  <text class="contact" x="610" y="53" text-anchor="end">4718 BRINDLE AVENUE,</text>
  <text class="contact" x="610" y="81" text-anchor="end">SASKATOON, SK, S4M 2J6</text>
  <text class="contact contact--phone" x="344" y="150" textLength="266" lengthAdjust="spacing">306-555-0148</text>
  <text class="contact contact--web" x="610" y="183" text-anchor="end">www.vault9nook.ca</text>
  <line class="divider" x1="628" y1="35" x2="628" y2="185"/>

  <!-- brand -->
  <rect class="brand__mark" x="724" y="40" width="62" height="62"/>
  <text class="brand__name" x="755" y="145" text-anchor="middle">VAULT 9 NOOK</text>
  <text class="brand__name" x="755" y="175" text-anchor="middle">STORAGE</text>

  <!-- TIRE column -->
  <text class="headline" x="812" y="402" text-anchor="middle">T</text>
  <text class="headline" x="812" y="592" text-anchor="middle">I</text>

  <!-- MOTOR row -->
  <text class="headline" x="268" y="776" textLength="478" lengthAdjust="spacingAndGlyphs">MOTO</text>
  <text class="headline" x="764" y="776">R</text>

  <!-- BICYCLE row -->
  <text class="headline" x="72" y="952">B</text>
  <text class="headline" x="190" y="952">I</text>
  <text class="headline headline--light" x="274" y="952" textLength="472" lengthAdjust="spacingAndGlyphs">CYCL</text>
  <text class="headline" x="772" y="952">E</text>

  <!-- motorcycle price -->
  <text class="price__amount" x="258" y="586" textLength="274" lengthAdjust="spacingAndGlyphs">$250</text>
  <text class="price__cents" x="540" y="530" textLength="108" lengthAdjust="spacingAndGlyphs">.00</text>
  <text class="price__note" x="667" y="578" text-anchor="end">/SEASON</text>
  <text class="price__note" x="667" y="609" text-anchor="end">+ TAX</text>

  <!-- bicycle price -->
  <text class="price__amount" x="48" y="1141" textLength="216" lengthAdjust="spacingAndGlyphs">$99</text>
  <text class="price__cents" x="266" y="1086" textLength="98" lengthAdjust="spacingAndGlyphs">.00</text>
  <text class="price__note" x="384" y="1124" text-anchor="end">/SEASON</text>
  <text class="price__note" x="384" y="1156" text-anchor="end">+ TAX</text>

  <!-- tire price -->
  <text class="price__amount" x="525" y="1141" textLength="216" lengthAdjust="spacingAndGlyphs">$99</text>
  <text class="price__cents" x="743" y="1086" textLength="98" lengthAdjust="spacingAndGlyphs">.00</text>
  <text class="price__note" x="861" y="1124" text-anchor="end">/SEASON</text>
  <text class="price__note" x="861" y="1156" text-anchor="end">+ TAX</text>
</svg>
</body>
</html>
```